Pelton|Marsh & Quillan business card contest

We need a logo for an upscale boutique diversified company involved in real estate, investments, cattle, and more. Our businesses DO NOT need to be reflected in the business card nor do we want them noted. This is our logo and colors and we love our logo and colors. Our logo looks best against a black background and we like to include the firm name in our logo usage. importantly, the names Pelton and Marsh are separated by | not / and we use an ampersand not the word and.
On the front of the card, we want to include:
company logo and name (Pelton|Marsh & Quillan)
on the back, we would definitely include:
address, email, cell #
logo and name (smaller size than front)

The variable will be location of individual name and title (mine for example is ) - whether on the front OR on the back. interested in variations from which to choose
Dr. Neil R. Whitcombe, CFA
Scientifique des Fusées Financières

we would like to use contemporary symbols for address, email address, cell # with an option for web site that we do not intend to use initially. we like two sided cards and believe this design should use four rounded corners with the standard size. we prefer thicker card stock and may look at metal.

```html
<!DOCTYPE html>
<html lang="en">
<head>
<meta charset="utf-8">
<title>Pelton|Marsh &amp; Quillan — Business Card</title>
<link rel="stylesheet" href="https://fonts.googleapis.com/css2?family=Open+Sans:wght@400;700&family=Cinzel:wght@400&display=swap">
<style>
  :root {
    --canvas: #ffffff;
    --stripe-front-a: #2c2c2c;
    --stripe-front-b: #3b3b3b;
    --stripe-back-a: #1b1b1b;
    --stripe-back-b: #232323;
    --brand-orange: #f07d12;
    --wordmark-grey: #707070;
    --label-bg: #262626;
    --contact-text: #e8e8e8;
  }
  html, body {
    margin: 0;
    padding: 0;
    width: 1200px;
    height: 1200px;
    overflow: hidden;
    background: var(--canvas);
  }
  .canvas {
    position: relative;
    width: 1200px;
    height: 1200px;
  }
  .card {
    position: absolute;
    width: 474px;
    height: 268px;
    overflow: hidden;
  }
  .card--front {
    left: 357px;
    top: 152px;
    background: repeating-linear-gradient(90deg,
      var(--stripe-front-a) 0 11px,
      var(--stripe-front-b) 11px 22px);
  }
  .card--back {
    left: 356px;
    top: 747px;
    background: repeating-linear-gradient(90deg,
      var(--stripe-back-a) 0 11px,
      var(--stripe-back-b) 11px 22px);
  }
  .brand-square {
    position: absolute;
    left: 50%;
    transform: translateX(-50%);
    background: var(--brand-orange);
  }
  .card--front .brand-square { top: 46px; width: 34px; height: 34px; }
  .card--back .brand-square { top: 72px; width: 26px; height: 26px; }
  .wordmark {
    position: absolute;
    left: 0;
    right: 0;
    text-align: center;
    font-family: "Open Sans", sans-serif;
    font-weight: 400;
    color: var(--wordmark-grey);
    white-space: nowrap;
  }
  .card--front .wordmark { top: 150px; font-size: 30px; letter-spacing: 0.5px; }
  .card--back .wordmark { top: 128px; font-size: 21px; }
  .holder-label {
    position: absolute;
    left: 153px;
    top: 226px;
    width: 166px;
    height: 20px;
    background: var(--label-bg);
    color: var(--brand-orange);
    font-family: "Open Sans", sans-serif;
    font-weight: 700;
    font-size: 11px;
    line-height: 20px;
    text-align: center;
    text-transform: uppercase;
    white-space: nowrap;
  }
  .contact-row {
    position: absolute;
    left: 22px;
    right: 18px;
    top: 239px;
    display: flex;
    align-items: center;
    gap: 10px;
    font-family: "Cinzel", serif;
    font-size: 8.5px;
    color: var(--contact-text);
    white-space: nowrap;
  }
  .contact-item {
    display: flex;
    align-items: center;
    gap: 4px;
  }
  .contact-item svg { display: block; fill: var(--contact-text); }
</style>
</head>
<body>
<main class="canvas">

  <section class="card card--front" aria-label="Card front">
    <div class="brand-square"></div>
    <div class="wordmark">Pelton|Marsh &amp; Quillan</div>
    <div class="holder-label">Dr. Neil R. Whitcombe, CFA</div>
  </section>

  <section class="card card--back" aria-label="Card back">
    <div class="brand-square"></div>
    <div class="wordmark">Pelton|Marsh &amp; Quillan</div>
    <div class="contact-row">
      <span class="contact-item">
        <svg width="13" height="9" viewBox="0 0 13 9" aria-hidden="true"><rect width="13" height="9" rx="1"/><path d="M0.8 0.8 L6.5 5 L12.2 0.8" fill="none" stroke="#1b1b1b" stroke-width="1"/></svg>
        mail@peltonmarshquillan.com
      </span>
      <span class="contact-item">
        <svg width="9" height="11" viewBox="0 0 24 24" aria-hidden="true"><path d="M6.6 10.8a15.1 15.1 0 0 0 6.6 6.6l2.2-2.2a1 1 0 0 1 1-.25 11.4 11.4 0 0 0 3.6.57 1 1 0 0 1 1 1V20a1 1 0 0 1-1 1A17 17 0 0 1 3 4a1 1 0 0 1 1-1h3.5a1 1 0 0 1 1 1c0 1.25.2 2.45.57 3.57a1 1 0 0 1-.25 1z"/></svg>
        014 275 61 38
      </span>
      <span class="contact-item">
        <svg width="11" height="11" viewBox="0 0 24 24" aria-hidden="true"><circle cx="12" cy="12" r="11"/><path d="M12 5a4.5 4.5 0 0 0-4.5 4.5C7.5 13 12 18 12 18s4.5-5 4.5-8.5A4.5 4.5 0 0 0 12 5zm0 6.2a1.7 1.7 0 1 1 0-3.4 1.7 1.7 0 0 1 0 3.4z" fill="#1b1b1b"/></svg>
        Address: Dummy address...............
      </span>
    </div>
  </section>

</main>
</body>
</html>
```